Venture firm needs flyer to attract Sales Professionals as Advisors

Creation of either a pdf Flyer or Brochure.
The target audience are senior sales professionals of the Information Technology industry. The flyer needs to come across highly professional, business oriented, positive. Text for the brochure is attached. The colors/graphics should align with Brindmore Capital corporate appearance: www.brindmore.capital

Target Market(s)

Sales Professionals in the Information Technology Industry

Industry/Entity Type

Information Technology

Font styles to use
• Raleway

Requirements
Must have
• fitting the corporate look and feel: www.brindmore.capital

```html
<!DOCTYPE html>
<html lang="en">
<head>
<meta charset="utf-8">
<title>Brindmore Sales Council Flyer</title>
<link rel="stylesheet" href="https://fonts.googleapis.com/css2?family=Anton&family=Source+Sans+3:wght@400;600;700&display=swap">
<style>
  :root {
    --navy: #0f3a66;
    --navy-deep: #0b2f55;
    --steel: #3c6d9c;
    --paper: #e6e9ee;
    --stage: #f3f1ed;
    --ink: #1c3557;
    --white: #ffffff;
    --ice-light: #c9d6e4;
    --ice-mid: #7f95b0;
    --ice-dark: #3b4e66;
  }
  * { box-sizing: border-box; margin: 0; padding: 0; }
  html, body {
    width: 1200px;
    height: 895px;
    overflow: hidden;
    background: var(--stage);
  }
  .canvas {
    position: relative;
    width: 1200px;
    height: 895px;
  }
  .flyer {
    position: absolute;
    top: 57px;
    width: 555px;
    height: 780px;
    overflow: hidden;
    box-shadow: 0 2px 10px rgba(0,0,0,0.12);
    font-family: "Source Sans 3", sans-serif;
  }
  .flyer-front { left: 30px; background: var(--paper); }
  .flyer-back { left: 615px; background: var(--white); }

  /* Front side */
  .flyer-header {
    height: 80px;
    background: var(--navy);
    display: flex;
    align-items: center;
    padding-left: 28px;
  }
  .brand-name {
    font-weight: 400;
    font-size: 22px;
    letter-spacing: 0.4px;
    color: var(--white);
  }
  .header-rule { height: 4px; background: var(--white); }
  .photo-area {
    background:
      radial-gradient(ellipse at 40% 85%, #f2f5f9 0%, rgba(242,245,249,0) 35%),
      radial-gradient(ellipse at 20% 40%, var(--ice-light) 0%, rgba(201,214,228,0) 45%),
      radial-gradient(ellipse at 75% 30%, var(--ice-mid) 0%, rgba(127,149,176,0) 50%),
      linear-gradient(160deg, var(--ice-dark) 0%, var(--ice-mid) 55%, var(--ice-light) 100%);
  }
  .hero-photo { height: 190px; }
  .title {
    text-align: center;
    color: var(--navy);
    padding-top: 8px;
    font-weight: 400;
  }
  .title-main {
    font-family: "Anton", sans-serif;
    font-size: 110px;
    line-height: 1;
    display: block;
  }
  .title-sub {
    font-family: "Anton", sans-serif;
    font-size: 50px;
    line-height: 1;
    display: block;
    margin-top: 4px;
  }
  .intro {
    padding: 14px 44px 0 44px;
    font-size: 12.4px;
    line-height: 22px;
    color: var(--ink);
    text-align: justify;
  }
  .flyer-footer {
    position: absolute;
    left: 0;
    bottom: 0;
    width: 100%;
    height: 14px;
    background: var(--navy-deep);
  }

  /* Back side */
  .back-top-band {
    position: absolute;
    left: 0; top: 0;
    width: 100%; height: 34px;
    background: var(--steel);
  }
  .back-photo {
    position: absolute;
    left: 300px; top: 34px;
    width: 255px; height: 566px;
  }
  .back-content {
    position: absolute;
    left: 0; top: 34px;
    width: 300px; height: 566px;
    padding: 16px 0 0 0;
  }
  .section-heading {
    background: var(--navy);
    color: var(--white);
    font-weight: 700;
    font-size: 17px;
    line-height: 30px;
    padding-left: 18px;
    margin-bottom: 8px;
  }
  .section-text {
    padding: 0 16px 0 22px;
    font-size: 11.2px;
    line-height: 15px;
    color: var(--ink);
    text-align: justify;
    margin-bottom: 6px;
  }
  .section + .section { margin-top: 12px; }
  .closing-band {
    position: absolute;
    left: 0; top: 600px;
    width: 100%; height: 80px;
    background: var(--steel);
    display: flex;
    align-items: center;
    padding: 0 26px;
  }
  .closing-text {
    color: var(--white);
    font-size: 13px;
    line-height: 19px;
  }
  .back-footer {
    position: absolute;
    left: 0; top: 680px;
    width: 100%; height: 100px;
    background: var(--navy);
    display: flex;
    align-items: center;
    padding-left: 28px;
  }
</style>
</head>
<body>
<div class="canvas">
  <article class="flyer flyer-front">
    <header class="flyer-header">
      <span class="brand-name">BRINDMORE CAPITAL</span>
    </header>
    <div class="header-rule"></div>
    <div class="photo-area hero-photo" role="img" aria-label="Photo of a climber in a yellow and green jacket standing on a snowy ridge above a frozen mountain lake"></div>
    <h1 class="title">
      <span class="title-main">Brindmore</span>
      <span class="title-sub">Sales Council (BSC)</span>
    </h1>
    <div class="intro">
      <p>The BSC is a by invitation only global community of high caliber Sales Professionals in the IT industry. Participating in the BSC provides significant wealth creation opportunities by earning consulting fees and sales commission or finding an exciting startup to work for.</p>
      <p>BSC members actively collaborate with each other to close deals, generate leads &amp; opportunities, navigate through client organizations and build a true advisory status with customers.</p>
      <p>BSC members get early first hand visibility into the latest technology innovations and learn how those technologies could assist their clients in solving their complex business objectives.</p>
    </div>
    <div class="flyer-footer"></div>
  </article>

  <article class="flyer flyer-back">
    <div class="back-top-band"></div>
    <div class="photo-area back-photo" role="img" aria-label="Photo of a climber with an ice axe on a snowy slope above a frozen landscape"></div>
    <div class="back-content">
      <section class="section">
        <h2 class="section-heading">How it works:</h2>
        <p class="section-text">BSC members will be introduced to Brindmore Capital's client and portfolio companies. This unique ability to learn about latest technology innovation keeps the participants up to date with industry trends and could open interesting earning or employment opportunities.</p>
        <p class="section-text">Once exposed to a specific vendor, BSC members can decide if and how they would like to get further involved. Dependent on the interest level for the specific technology, the ability to offer a solution to a known customer problem or the sheer interest to develop new business, BSC members can participate in two ways:</p>
      </section>
      <section class="section">
        <h2 class="section-heading">As Associates:</h2>
        <p class="section-text">Associates are actively selling and promoting one or more Brindmore Capital portfolio companies. This could be an employment or a freelance opportunity.</p>
      </section>
      <section class="section">
        <h2 class="section-heading">As Advisors:</h2>
        <p class="section-text">Advisors offer their contacts and knowledge about customers to Associates. Advisors could create leads, support with introductions, explain customer organization and processes etc. They will be compensated by Associates with a pre-negotiated % of commission of a future sale that was supported by the Advisor.</p>
      </section>
    </div>
    <div class="closing-band">
      <p class="closing-text">Whatever level of involvement a BSC member seeks there is plenty of opportunity to be rewarded for working with fellow Sales Professionals and Great Startups on the forefront of technical innovation.</p>
    </div>
    <footer class="back-footer">
      <span class="brand-name">BRINDMORE CAPITAL</span>
    </footer>
  </article>
</div>
</body>
</html>
```